Report template for evaluation reports to be used by non designers

We are looking for a report template that meets all the requirements listed in the attached documents. letter head, logo etc have been enclosed. Its important that the colour integrity is kept, but beyond that options are welcome.
Its important that the document is extremely easy to use and that is able to be adapted to include eatables, figures, pictures, text boxes etc and keep the integrity of the template

Target Market(s)

Governments, Civil society organisations and research institutions

Font styles to use
Sans Serif

Colors
6b449b
876aae
c0c0c0
000000

Requirements
Must have
• Clean, professional, not concluded, modern, must be easy to use
Should not have
• too busy, hard to use

```html
<!DOCTYPE html>
<html lang="en">
<head>
<meta charset="utf-8">
<title>Word Template – Report Layout</title>
<link rel="stylesheet" href="https://fonts.googleapis.com/css2?family=Anton&family=Open+Sans:wght@400;600;700;800&display=swap">
<style>
  :root {
    --purple: #5c4fa2;
    --purple-soft: #876aae;
    --lavender: #ece9f6;
    --link-blue: #3b3a9c;
    --board: #d4d4d4;
    --ink: #111111;
    --grey: #c0c0c0;
    --icon-bg: #e9e9ec;
    --white: #ffffff;
  }
  * { box-sizing: border-box; margin: 0; padding: 0; }
  html, body { width: 1200px; height: 2624px; overflow: hidden; }
  body {
    background: var(--board);
    font-family: "Open Sans", Arial, sans-serif;
    color: var(--ink);
    position: relative;
  }
  .board-title {
    position: absolute; top: 22px; left: 0; width: 1200px;
    text-align: center; font-size: 38px; font-weight: 400; letter-spacing: 1px; color: #1d2330;
  }
  .page {
    position: absolute; width: 546px; height: 775px;
    background: var(--white); overflow: hidden;
    box-shadow: 0 1px 4px rgba(0,0,0,.25);
  }
  .page-label {
    position: absolute; width: 546px; text-align: center;
    font-size: 24px; color: #222;
  }
  .deco { position: absolute; left: 0; top: 0; }

  /* wordmark: one weight, one colour, one plain circle */
  .brand {
    position: absolute; display: flex; align-items: center; gap: 10px;
    font-weight: 700; line-height: 1; white-space: nowrap;
  }
  .brand-dot { border-radius: 50%; background: var(--purple); flex: none; }

  /* cover */
  .cover-title {
    position: absolute; right: 26px; top: 20px; text-align: right;
    font-family: "Anton", "Open Sans", sans-serif; font-size: 104px; line-height: 1; color: var(--ink);
  }
  .cover-subtitle {
    position: absolute; right: 26px; top: 128px;
    font-size: 50px; font-weight: 800; color: var(--purple); letter-spacing: -1px; line-height: 1;
  }
  .cover-date {
    position: absolute; right: 26px; top: 190px;
    font-size: 28px; letter-spacing: 3px; color: var(--ink);
  }
  .cover-brand { left: 26px; top: 470px; font-size: 30px; color: var(--ink); }
  .cover-brand .brand-dot { width: 26px; height: 26px; }
  .client-name {
    position: absolute; left: 0; width: 546px; top: 672px; text-align: center;
    color: var(--white); font-size: 33px; font-weight: 700;
  }
  .web-address {
    position: absolute; left: 0; width: 546px; top: 734px; text-align: center;
    color: var(--white); font-size: 14px; letter-spacing: 2px;
  }

  /* inner pages */
  .running-head {
    position: absolute; left: 26px; top: 20px; right: 0;
    display: flex; align-items: center; gap: 12px;
    color: var(--purple); font-size: 17px; font-weight: 700; white-space: nowrap;
  }
  .running-head::after { content: ""; flex: 1; height: 2px; background: var(--purple); }
  .section-heading {
    position: absolute; left: 26px; color: var(--purple); font-size: 19px; font-weight: 700;
  }
  .toc-heading { top: 105px; font-size: 17px; }
  .toc-marker { position: absolute; left: 0; top: 108px; width: 9px; height: 20px; background: var(--purple); }
  .toc-list { position: absolute; left: 26px; top: 145px; width: 488px; list-style: none; }
  .toc-entry { display: flex; align-items: center; height: 34px; font-size: 13px; }
  .toc-entry .leader { flex: 1; border-bottom: 2px dotted #777; margin: 0 18px 0 26px; height: 0; }
  .footnotes { position: absolute; left: 26px; top: 640px; width: 494px; font-size: 12px; }
  .footnote-rule { height: 1.5px; background: #444; margin-top: 16px; }
  .footnote-rule + .footnote-rule { margin-top: 22px; }
  .page-foot { position: absolute; left: 26px; right: 26px; top: 724px; display: flex; align-items: center; gap: 8px; }
  .foot-brand { position: static; font-size: 10px; color: var(--ink); gap: 4px; }
  .foot-brand .brand-dot { width: 8px; height: 8px; }
  .page-foot .rule { flex: 1; height: 2px; background: var(--purple); }
  .page-foot .num { font-size: 11px; }
  .body-copy { position: absolute; left: 26px; width: 494px; font-size: 10.5px; line-height: 13px; text-align: justify; }
  .feature-icons { position: absolute; left: 0; top: 222px; width: 546px; }
  .feature { position: absolute; width: 170px; text-align: center; }
  .feature-circle {
    width: 70px; height: 70px; border-radius: 50%; background: var(--icon-bg);
    margin: 0 auto; display: flex; align-items: center; justify-content: center;
  }
  .feature-caption { margin-top: 18px; font-size: 11px; font-weight: 700; color: var(--purple); }
  .bullet-list { position: absolute; left: 26px; top: 350px; width: 494px; list-style: none; font-size: 11px; line-height: 15px; }
  .bullet-list li { position: relative; padding-left: 16px; margin-bottom: 12px; text-align: justify; }
  .bullet-list li::before {
    content: ""; position: absolute; left: 0; top: 5px; width: 6px; height: 6px; border-radius: 50%; background: var(--purple);
  }
  .callout { position: absolute; left: 26px; top: 474px; width: 494px; background: var(--lavender); padding: 7px 9px; }
  .callout p { font-size: 10.5px; line-height: 13px; text-align: justify; }

  .step-box { position: absolute; left: 0; width: 520px; height: 96px; border: 2px solid var(--purple); display: flex; }
  .step-num { width: 96px; background: var(--purple); display: flex; align-items: center; justify-content: center; }
  .step-num span {
    width: 38px; height: 38px; border-radius: 50%; border: 3px solid var(--white);
    color: var(--white); font-weight: 700; font-size: 20px; display: flex; align-items: center; justify-content: center;
  }
  .step-items { list-style: none; padding: 14px 0 0 20px; font-size: 10.5px; }
  .step-items li { display: flex; align-items: center; gap: 8px; height: 23px; }
  .photo-band {
    position: absolute; left: 0; top: 330px; width: 546px; height: 206px;
    background: linear-gradient(100deg, #cfd3da 0%, #9aa4b4 35%, #d8c9be 65%, #7a6d78 100%);
    border-top-right-radius: 70px;
  }
  .photo-rule { position: absolute; left: 0; top: 536px; width: 546px; height: 5px; background: var(--purple); }

  /* back page */
  .contact-head {
    position: absolute; left: 0; top: 70px; width: 546px;
    display: flex; align-items: center; gap: 14px;
    color: var(--purple); font-size: 28px; font-weight: 700;
  }
  .contact-head::before, .contact-head::after { content: ""; flex: 1; height: 2px; background: var(--purple); }
  .map-area { position: absolute; left: 0; top: 118px; width: 546px; height: 290px; background: linear-gradient(180deg, #f4f4f6, #fafafa); }
  .contact-icons { position: absolute; top: 131px; left: 0; width: 546px; display: flex; justify-content: center; gap: 16px; }
  .contact-icon { width: 28px; height: 28px; border-radius: 50%; background: var(--purple); display: flex; align-items: center; justify-content: center; }
  .contact-lines { position: absolute; top: 178px; left: 0; width: 546px; list-style: none; text-align: center; font-size: 17px; color: var(--link-blue); }
  .contact-lines li { height: 44px; }
  .back-brand { left: 0; width: 546px; top: 620px; justify-content: center; font-size: 36px; color: var(--white); }
  .back-brand .brand-dot { width: 30px; height: 30px; background: var(--white); }
  .board-brand { left: 650px; top: 2130px; width: 470px; justify-content: center; font-size: 38px; color: var(--ink); }
  .board-brand .brand-dot { width: 32px; height: 32px; }
</style>
</head>
<body>
  <h1 class="board-title">WORD TEMPLATE</h1>

  <!-- Cover page -->
  <section class="page cover" style="left:40px; top:107px;">
    <svg class="deco" width="546" height="775" viewBox="0 0 546 775">
      <rect x="0" y="0" width="12" height="420" fill="var(--purple)"/>
      <polygon points="0,610 546,528 546,538 0,620" fill="var(--purple)"/>
      <polygon points="0,640 546,560 546,775 0,775" fill="var(--purple)"/>
    </svg>
    <div class="cover-title">TITLE OF</div>
    <div class="cover-subtitle">THE REPORT</div>
    <div class="cover-date">Date, Month, Year</div>
    <div class="brand cover-brand"><span class="brand-dot"></span>Brennholt Evidence Lab</div>
    <div class="client-name">CLIENT NAME</div>
    <div class="web-address">www.brennholt-evidence.org</div>
  </section>
  <div class="page-label" style="left:40px; top:894px;">COVER PAGE</div>

  <!-- Page 02: contents -->
  <section class="page contents" style="left:616px; top:107px;">
    <div class="running-head">THE NAME OF THE REPORT</div>
    <span class="toc-marker"></span>
    <h2 class="section-heading toc-heading">TABLE OF CONTENTS</h2>
    <ol class="toc-list">
      <li class="toc-entry">Lorem Ipsum is simply<span class="leader"></span>03</li>
      <li class="toc-entry">Lorem Ipsum is simply<span class="leader"></span>04</li>
      <li class="toc-entry">Lorem Ipsum is simply<span class="leader"></span>05</li>
      <li class="toc-entry">Lorem Ipsum is simply<span class="leader"></span>06</li>
      <li class="toc-entry">Lorem Ipsum is simply<span class="leader"></span>07</li>
      <li class="toc-entry">Lorem Ipsum is simply<span class="leader"></span>08</li>
      <li class="toc-entry">Lorem Ipsum is simply<span class="leader"></span>09</li>
    </ol>
    <div class="footnotes">FOOTNOTES<div class="footnote-rule"></div><div class="footnote-rule"></div></div>
    <div class="page-foot"><div class="brand foot-brand"><span class="brand-dot"></span>Brennholt Evidence Lab</div><span class="rule"></span><span class="num">02</span></div>
  </section>
  <div class="page-label" style="left:616px; top:894px;">PAGE - 02</div>

  <!-- Page 03: text and features -->
  <section class="page text-page" style="left:40px; top:946px;">
    <div class="running-head">THE NAME OF THE REPORT</div>
    <h2 class="section-heading" style="top:64px;">HEADING GOES HERE</h2>
    <p class="body-copy" style="top:96px;">Lorem Ipsum is simply dummy text of the printing and typesetting industry. Lorem Ipsum has been the industry's standard dummy text ever since the 1500s, when an unknown printer took a galley of type and scrambled it to make a type specimen book. It has survived not only five centuries, but also the leap into electronic typesetting, remaining essentially unchanged. It was popularised in the 1960s with the release of Letraset sheets containing Lorem Ipsum passages, and more recently with desktop publishing software like Aldus PageMaker including versions of Lorem Ipsum.</p>
    <div class="feature-icons">
      <div class="feature" style="left:6px;">
        <div class="feature-circle">
          <svg width="36" height="30" viewBox="0 0 36 30" fill="var(--purple)"><circle cx="18" cy="6" r="4"/><circle cx="8" cy="11" r="3.5"/><circle cx="28" cy="11" r="3.5"/><path d="M11 24 Q18 10 25 24Z"/><path d="M2 28 Q8 16 14 28Z"/><path d="M22 28 Q28 16 34 28Z"/></svg>
        </div>
        <div class="feature-caption">Lorem Ipsum is simply dummy</div>
      </div>
      <div class="feature" style="left:186px;">
        <div class="feature-circle">
          <svg width="30" height="32" viewBox="0 0 30 32" fill="var(--purple)"><rect x="3" y="6" width="12" height="26"/><rect x="17" y="0" width="11" height="32"/><g fill="var(--icon-bg)"><rect x="6" y="10" width="3" height="3"/><rect x="10" y="10" width="3" height="3"/><rect x="6" y="16" width="3" height="3"/><rect x="10" y="16" width="3" height="3"/><rect x="20" y="5" width="5" height="2"/><rect x="20" y="10" width="5" height="2"/><rect x="20" y="15" width="5" height="2"/><rect x="20" y="20" width="5" height="2"/></g></svg>
        </div>
        <div class="feature-caption">Lorem Ipsum is simply text</div>
      </div>
      <div class="feature" style="left:364px;">
        <div class="feature-circle">
          <svg width="34" height="30" viewBox="0 0 34 30" fill="var(--purple)"><rect x="13" y="0" width="8" height="8"/><rect x="1" y="20" width="8" height="8"/><rect x="13" y="20" width="8" height="8"/><rect x="25" y="20" width="8" height="8"/><path d="M16 8h2v5h12v7h-2v-5H18v5h-2v-5H6v5H4v-7h12z"/></svg>
        </div>
        <div class="feature-caption">Lorem Ipsum is simply dummy</div>
      </div>
    </div>
    <ul class="bullet-list">
      <li>Lorem Ipsum is simply dummy text of the printing and typesetting industry. Lorem Ipsum has been the industry's standard dummy text ever since the 1500s.</li>
      <li>Lorem Ipsum is simply dummy text of the printing and typesetting industry.</li>
    </ul>
    <h2 class="section-heading" style="top:442px;">HEADING GOES HERE</h2>
    <div class="callout"><p>Lorem Ipsum is simply dummy text of the printing and typesetting industry. Lorem Ipsum has been the industry's standard dummy text ever since the 1500s, when an unknown printer took a galley of type and scrambled it to make a type specimen book. It has survived not only five centuries, but also the leap into electronic typesetting, remaining essentially unchanged. It was popularised in the 1960s with the release of Letraset sheets containing Lorem Ipsum passages, and more recently with desktop publishing software like Aldus PageMaker including versions of Lorem Ipsum.</p></div>
    <div class="footnotes">FOOTNOTES<div class="footnote-rule"></div><div class="footnote-rule"></div></div>
    <div class="page-foot"><div class="brand foot-brand"><span class="brand-dot"></span>Brennholt Evidence Lab</div><span class="rule"></span><span class="num">03</span></div>
  </section>
  <div class="page-label" style="left:40px; top:1733px;">PAGE - 03</div>

  <!-- Page 04: steps and photo -->
  <section class="page steps-page" style="left:616px; top:946px;">
    <div class="running-head">THE NAME OF THE REPORT</div>
    <h2 class="section-heading" style="top:64px;">HEADING GOES HERE</h2>
    <div class="step-box" style="top:108px;">
      <div class="step-num"><span>1</span></div>
      <ul class="step-items">
        <li><svg width="10" height="10" viewBox="0 0 10 10"><circle cx="5" cy="5" r="4.3" fill="none" stroke="var(--purple)"/><path d="M3 5l1.5 1.5L7 3.8" fill="none" stroke="var(--purple)"/></svg>Lorem Ipsum is simply dummy text of the printing and typesetting industry.</li>
        <li><svg width="10" height="10" viewBox="0 0 10 10"><circle cx="5" cy="5" r="4.3" fill="none" stroke="var(--purple)"/><path d="M3 5l1.5 1.5L7 3.8" fill="none" stroke="var(--purple)"/></svg>Lorem Ipsum is simply dummy text of the printing and typesetting industry.</li>
        <li><svg width="10" height="10" viewBox="0 0 10 10"><circle cx="5" cy="5" r="4.3" fill="none" stroke="var(--purple)"/><path d="M3 5l1.5 1.5L7 3.8" fill="none" stroke="var(--purple)"/></svg>Lorem Ipsum is simply dummy text of the printing and typesetting industry.</li>
      </ul>
    </div>
    <div class="step-box" style="top:216px;">
      <div class="step-num"><span>2</span></div>
      <ul class="step-items">
        <li><svg width="10" height="10" viewBox="0 0 10 10"><circle cx="5" cy="5" r="4.3" fill="none" stroke="var(--purple)"/><path d="M3 5l1.5 1.5L7 3.8" fill="none" stroke="var(--purple)"/></svg>Lorem Ipsum is simply dummy text of the printing and typesetting industry.</li>
        <li><svg width="10" height="10" viewBox="0 0 10 10"><circle cx="5" cy="5" r="4.3" fill="none" stroke="var(--purple)"/><path d="M3 5l1.5 1.5L7 3.8" fill="none" stroke="var(--purple)"/></svg>Lorem Ipsum is simply dummy text of the printing and typesetting industry.</li>
        <li><svg width="10" height="10" viewBox="0 0 10 10"><circle cx="5" cy="5" r="4.3" fill="none" stroke="var(--purple)"/><path d="M3 5l1.5 1.5L7 3.8" fill="none" stroke="var(--purple)"/></svg>Lorem Ipsum is simply dummy text of the printing and typesetting industry.</li>
      </ul>
    </div>
    <div class="photo-band" role="img" aria-label="Photo of colleagues talking together in a meeting"></div>
    <div class="photo-rule"></div>
    <div class="footnotes">FOOTNOTES<div class="footnote-rule"></div><div class="footnote-rule"></div></div>
    <div class="page-foot"><div class="brand foot-brand"><span class="brand-dot"></span>Brennholt Evidence Lab</div><span class="rule"></span><span class="num">04</span></div>
  </section>
  <div class="page-label" style="left:616px; top:1733px;">PAGE - 04</div>

  <!-- Back page -->
  <section class="page back" style="left:40px; top:1786px;">
    <div class="map-area" role="img" aria-label="Faint world map in the background"></div>
    <h2 class="contact-head">CONTACT US</h2>
    <div class="contact-icons">
      <span class="contact-icon"><svg width="12" height="15" viewBox="0 0 12 15"><path d="M6 0a6 6 0 0 0-6 6c0 4.5 6 9 6 9s6-4.5 6-9a6 6 0 0 0-6-6z" fill="#fff"/><circle cx="6" cy="6" r="2.2" fill="var(--purple)"/></svg></span>
      <span class="contact-icon"><svg width="14" height="14" viewBox="0 0 14 14"><path d="M3 0l3 3.5-2 2a8 8 0 0 0 4.5 4.5l2-2L14 11l-2 3C5 14 0 9 0 2z" fill="#fff"/></svg></span>
      <span class="contact-icon"><svg width="14" height="10" viewBox="0 0 14 10"><rect x="0.5" y="0.5" width="13" height="9" fill="none" stroke="#fff"/><path d="M0.5 0.5L7 5.5l6.5-5" fill="none" stroke="#fff"/></svg></span>
    </div>
    <ul class="contact-lines">
      <li>Address Goes Here</li>
      <li>Phone No Goes Here</li>
      <li>E-mail Goes Here</li>
    </ul>
    <svg class="deco" width="546" height="775" viewBox="0 0 546 775">
      <polygon points="0,548 546,462 546,472 0,558" fill="var(--purple)"/>
      <polygon points="0,578 546,494 546,775 0,775" fill="var(--purple)"/>
    </svg>
    <div class="brand back-brand"><span class="brand-dot"></span>Brennholt Evidence Lab</div>
    <div class="web-address">www.brennholt-evidence.org</div>
  </section>
  <div class="page-label" style="left:40px; top:2573px;">BACK PAGE</div>

  <div class="brand board-brand"><span class="brand-dot"></span>Brennholt Evidence Lab</div>
</body>
</html>
```